Marrowgate Auctions Business Cards Design Needed

I need a business card design that is modern looking - double sided (maybe just my logo on the back, but open to suggestions) - the overall design is up to you. I want it to be easy to read - not over the top flashy. I already have a company logo which I uploaded so that needs to be used. The colors of my logo are the colors I want on the card... so blue and gray (do need to match the logo colors).

Requirements
Must have
• Would like the card to be sleek, modern and easy to ready

```html
<!DOCTYPE html>
<html lang="en">
<head>
<meta charset="utf-8">
<title>Marrowgate Auctions – Business Cards</title>
<link href="https://fonts.googleapis.com/css2?family=Ubuntu:wght@400;500;700&display=swap" rel="stylesheet">
<style>
  :root {
    --backdrop: #2b2b2b;
    --card-white: #f3f3f3;
    --brand-blue: #2a78b8;
    --brand-gray: #4a4a4a;
    --text-gray: #3c3c3c;
    --white: #ffffff;
  }
  * { margin: 0; padding: 0; box-sizing: border-box; }
  html, body {
    width: 1200px; height: 1050px; overflow: hidden;
    background: var(--backdrop);
    font-family: "Ubuntu", sans-serif;
  }
  .canvas { position: relative; width: 1200px; height: 1050px; }
  .card {
    position: absolute; left: 255px; width: 690px; height: 394px;
    box-shadow: 0 6px 18px rgba(0,0,0,0.55);
  }
  .card-front { top: 103px; background: var(--card-white); }
  .card-back { top: 555px; background: var(--brand-blue); color: var(--white); }

  .front-brand {
    position: absolute; right: 40px; top: 120px;
    display: flex; align-items: center; gap: 10px;
  }
  .brand-square { width: 16px; height: 16px; background: var(--brand-blue); }
  .brand-name {
    font-weight: 700; font-size: 29px; color: var(--brand-blue);
    letter-spacing: 0.2px;
  }

  .person { position: absolute; left: 42px; top: 222px; }
  .person-name {
    font-weight: 500; font-size: 30px; color: var(--brand-blue);
    letter-spacing: 0.3px; line-height: 1.1;
  }
  .person-title { font-size: 19px; color: var(--text-gray); margin-top: 2px; }
  .person-rule { width: 43px; height: 3px; background: var(--brand-blue); margin-top: 14px; }

  .contacts { list-style: none; margin-top: 20px; }
  .contacts li {
    display: flex; align-items: center; gap: 8px;
    font-size: 18.5px; color: var(--text-gray); line-height: 21px;
  }
  .contacts svg { width: 14px; height: 14px; flex: none; }

  .back-brand {
    position: absolute; left: 0; right: 0; top: 170px;
    display: flex; justify-content: center; align-items: center; gap: 12px;
  }
  .back-brand .brand-square { width: 22px; height: 22px; background: var(--white); }
  .back-brand .brand-name { color: var(--white); font-size: 40px; }
  .tagline {
    position: absolute; left: 0; right: 0; top: 332px;
    text-align: center; font-size: 21px; letter-spacing: 0.2px;
  }
</style>
</head>
<body>
<main class="canvas">
  <section class="card card-front">
    <div class="front-brand">
      <span class="brand-square"></span>
      <span class="brand-name">Marrowgate Auctions</span>
    </div>
    <div class="person">
      <h1 class="person-name">OWEN PRATLEY</h1>
      <p class="person-title">Owner/President - Auctioneer</p>
      <div class="person-rule"></div>
      <ul class="contacts">
        <li>
          <svg viewBox="0 0 16 16" aria-hidden="true"><path fill="#2a78b8" d="M3.5 1.5l2.5 3-1.5 1.8c.9 1.9 2.3 3.3 4.2 4.2l1.8-1.5 3 2.5-1.6 2.3C7 13.5 2.5 9 1.2 3.1z"/></svg>
          555-014-2738
        </li>
        <li>
          <svg viewBox="0 0 16 16" aria-hidden="true"><rect x="1.5" y="3.5" width="13" height="9" fill="none" stroke="#2a78b8" stroke-width="1.4"/><path d="M1.5 3.5l6.5 5 6.5-5" fill="none" stroke="#2a78b8" stroke-width="1.4"/></svg>
          hello@marrowgate.com
        </li>
        <li>
          <svg viewBox="0 0 16 16" aria-hidden="true"><circle cx="8" cy="8" r="6.5" fill="#2a78b8"/><path d="M1.5 8h13M8 1.5c-2.5 3-2.5 10 0 13M8 1.5c2.5 3 2.5 10 0 13" fill="none" stroke="#f3f3f3" stroke-width="1.1"/></svg>
          www.bidharbor.com
        </li>
      </ul>
    </div>
  </section>

  <section class="card card-back">
    <div class="back-brand">
      <span class="brand-square"></span>
      <span class="brand-name">Marrowgate Auctions</span>
    </div>
    <p class="tagline">Improving Charity Auctions Nationwide</p>
  </section>
</main>
</body>
</html>
```